Website Online Research Solutions

We are a small European high-tech online research company.
With our own state of the art software we run online panels and are conducting reseach for companies. Partly research via our own panel and partly via panels we maintain for our customers.
Our current website is old and outdatet: www.pravelo.nl.
We are in the process to change the content of the site. We want a modern, european and businesslike design for our new website.
Our logo has to stay the same (left uppersite of our website and attached) but can be changed a little to adapt it to the new design of the website. The colors of the site are up to you.
Target Market(s)
Marketeers and researchers of large and middle size companies in all kind of fields.
Industry/Entity Type
Online
Look and feel
Each slider illustrates characteristics of the customer's brand and the style your logo design should communicate.

```html
<!DOCTYPE html>
<html lang="en">
<head>
<meta charset="utf-8">
<title>Pravelo – Online Research Solutions</title>
<link rel="stylesheet" href="https://fonts.googleapis.com/css2?family=PT+Sans:wght@400;700&family=Arimo:ital,wght@0,400;1,400&family=Kalam:wght@400&display=swap">
<style>
  :root {
    --bg-deep: #0c1720;
    --bg-glow: #2b4a5d;
    --nav-active: #8a3333;
    --text-light: #ffffff;
    --text-muted: #d6dde3;
    --hero-panel: rgba(40, 98, 170, 0.93);
    --btn-top: #f7b21a;
    --btn-bottom: #e08d00;
    --btn-text: #3b2400;
    --footer-top: #1b355c;
    --footer-bottom: #2f5a9c;
    --rule: #c9d0d6;
  }
  * { box-sizing: border-box; margin: 0; padding: 0; }
  html, body { width: 1200px; height: 950px; overflow: hidden; }
  body {
    position: relative;
    font-family: "Arimo", Arial, sans-serif;
    color: var(--text-light);
    background:
      radial-gradient(ellipse 700px 520px at 600px 260px, var(--bg-glow) 0%, #1a3140 45%, var(--bg-deep) 100%);
  }
  .abs { position: absolute; }

  /* Brand */
  .brand { left: 124px; top: 24px; width: 112px; height: 96px; display: flex; align-items: center; gap: 8px; }
  .brand-dot { width: 14px; height: 14px; border-radius: 50%; background: var(--text-light); flex: none; }
  .brand-name { font-family: "PT Sans", sans-serif; font-weight: 700; font-size: 26px; color: var(--text-light); }

  /* Navigation */
  .main-nav { left: 498px; top: 0; height: 69px; display: flex; }
  .main-nav a {
    font-family: "PT Sans", sans-serif; font-size: 15px; color: var(--text-light);
    text-decoration: none; text-transform: uppercase; line-height: 84px; height: 69px; display: block;
  }
  .main-nav .home { background: var(--nav-active); width: 72px; text-align: center; }
  .main-nav .about { margin-left: 19px; }
  .main-nav .demos { margin-left: 38px; }
  .main-nav .media { margin-left: 36px; }
  .main-nav .customers { margin-left: 32px; }
  .main-nav .contact { margin-left: 31px; }

  .contact-info { left: 497px; top: 101px; font-size: 12px; line-height: 19px; }
  .social { top: 105px; width: 30px; height: 30px; border-radius: 5px; }
  .social.one { left: 727px; background: #3b5a9a; }
  .social.two { left: 768px; background: #3fb3e0; }
  .social.three { left: 808px; background: #f07a10; }

  .search { left: 855px; top: 99px; width: 225px; height: 40px; border-radius: 5px; background: #fff;
    box-shadow: inset 0 2px 4px rgba(0,0,0,.45); border: 2px solid #c2c8cd; }
  .search span { position: absolute; left: 13px; top: 11px; font-size: 13px; color: #333; }
  .search .go { position: absolute; right: 0; top: 0; width: 40px; height: 36px; background: linear-gradient(#f2f4f6, #cfd5da); border-left: 1px solid #b8bec4; border-radius: 0 3px 3px 0; }

  /* Hero */
  .hero { left: 119px; top: 150px; width: 961px; height: 293px; border-radius: 6px; overflow: hidden;
    background: linear-gradient(90deg, #d9dcd8 0%, #f1ece2 30%, #e9e4d6 55%, #cfd3d4 80%, #b8c0c6 100%); }
  .hero-panel { left: 606px; top: 172px; width: 474px; height: 178px; background: var(--hero-panel); padding: 18px 16px; font-family: "PT Sans", sans-serif; }
  .hero-panel h1 { font-weight: 400; font-size: 29px; line-height: 34px; margin-bottom: 9px; }
  .hero-panel p { font-size: 19px; line-height: 24px; }
  .hero-panel p + p { margin-top: 16px; }
  .hero-panel a { color: var(--text-light); }

  /* Columns */
  .col-title { top: 477px; font-family: "PT Sans", sans-serif; font-weight: 400; font-size: 32px; }
  .col-photo { top: 526px; width: 300px; height: 122px; }
  .photo-office { left: 124px; background: linear-gradient(100deg, #5a4a3a 0%, #c9b9a0 35%, #e7e3dc 60%, #6c6a66 100%); }
  .photo-team { left: 458px; background: linear-gradient(180deg, #7a4634 0%, #5b3a30 40%, #3c3a3a 70%, #9a958b 100%); }
  .col-text { top: 663px; width: 300px; font-size: 12px; line-height: 14.5px; }

  .btn { height: 29px; border-radius: 4px; background: linear-gradient(var(--btn-top), var(--btn-bottom));
    color: var(--btn-text); font-size: 12px; text-align: center; line-height: 29px; text-decoration: none;
    border: 1px solid #b87200; }

  .quote { left: 794px; width: 270px; font-family: "Kalam", cursive; font-size: 13.5px; line-height: 15.3px; letter-spacing: .3px; }
  .quote-by { width: 264px; left: 794px; text-align: right; font-style: italic; font-size: 12px; line-height: 15px; color: var(--text-muted); }
  .quote-rule { left: 794px; top: 680px; width: 264px; height: 1px; background: var(--rule); }

  /* Footer */
  .site-footer { left: 0; top: 881px; width: 1200px; height: 69px; border-top: 1px solid #5b7598;
    background: linear-gradient(var(--footer-top), var(--footer-bottom)); font-size: 12px; }
  .site-footer .copy { position: absolute; left: 141px; top: 30px; }
  .site-footer .divider { position: absolute; left: 339px; top: 27px; width: 1px; height: 21px; background: #6f88ad; }
  .site-footer a { position: absolute; left: 352px; top: 30px; color: var(--text-light); }
</style>
</head>
<body>
  <header>
    <div class="abs brand"><span class="brand-dot"></span><span class="brand-name">Pravelo</span></div>
    <nav class="abs main-nav">
      <a class="home" href="#">Home</a>
      <a class="about" href="#">About us</a>
      <a class="demos" href="#">Demos</a>
      <a class="media" href="#">Media</a>
      <a class="customers" href="#">Our customers</a>
      <a class="contact" href="#">Contact</a>
    </nav>
    <div class="abs contact-info">Havenstraat 12 1131 BK Edam<br>+31 (0)299 480210 - info@pravelo.nl</div>
    <span class="abs social one" role="img" aria-label="Social network link"></span>
    <span class="abs social two" role="img" aria-label="Social network link"></span>
    <span class="abs social three" role="img" aria-label="News feed link"></span>
    <div class="abs search">
      <span>Search...</span>
      <div class="go">
        <svg width="40" height="36" viewBox="0 0 40 36" aria-hidden="true">
          <circle cx="18" cy="16" r="7" fill="#e8f2fa" stroke="#6a7c8c" stroke-width="2"/>
          <line x1="23" y1="21" x2="29" y2="27" stroke="#6a7c8c" stroke-width="3" stroke-linecap="round"/>
        </svg>
      </div>
    </div>
  </header>

  <section>
    <div class="abs hero" role="img" aria-label="Photo of smiling research team members in a bright office"></div>
    <div class="abs hero-panel">
      <h1>Hello! We are Pravelo.</h1>
      <p>We specialize in online data collection<br>and analysis and we work for international clients.</p>
      <p>You can check a list of our <a href="#">happy clients</a>.</p>
    </div>
  </section>

  <main>
    <h2 class="abs col-title" style="left:124px">What we do</h2>
    <div class="abs col-photo photo-office" role="img" aria-label="Photo of the team working at desks in the office"></div>
    <p class="abs col-text" style="left:124px">Praesent nunc velit, commodo sit amet bibendum eu, dignissim eget erat. Aliquam sed ante id lacus convallis convallis sit amet nec lectus. Nulla rutrum varius risus, vitae posuere augue scelerisque quis.<br>Sed sed adipiscing tortor</p>
    <a class="abs btn" href="#" style="left:296px;top:760px;width:127px">Continue Reading »</a>

    <h2 class="abs col-title" style="left:458px">Who we are</h2>
    <div class="abs col-photo photo-team" role="img" aria-label="Group photo of the team standing outside a brick building"></div>
    <p class="abs col-text" style="left:458px">Vestibulum vulputate risus in dui tempor ac ultrices sapien volutpat. Curabitur dapibus vestibulum purus. Donec pulvinar lorem at justo cursus in laoreet risus porttitor. Etiam eget dolor non diam fermentum lobortis sed ut libero. Morbi ut lacus est. Pellentesque quis.</p>
    <a class="abs btn" href="#" style="left:631px;top:760px;width:127px">Continue Reading »</a>

    <h2 class="abs col-title" style="left:791px">Testimonials</h2>
    <blockquote class="abs quote" style="top:523px">"Het is een verademing om met Pravelo te werken in vergelijking met andere onderzoeksbureaus. Je hoeft iets maar één keer uit te leggen, ze denken op een goede en prettige manier mee en de kwaliteit is prima in orde. Ik ben, kortom, zeer tevreden."</blockquote>
    <p class="abs quote-by" style="top:640px">Marit de Vos<br>Research Director Merkwijzer</p>
    <div class="abs quote-rule"></div>
    <blockquote class="abs quote" style="top:697px">"Na onze test is gebleken: Het panel van Pravelo is een van de beste en een van de meest representatieve panels in Nederland."</blockquote>
    <p class="abs quote-by" style="top:768px">Joris Bakker - Kwadrant Insights</p>
    <a class="abs btn" href="#" style="left:931px;top:798px;width:127px">Other Testimonials »</a>
  </main>

  <footer class="abs site-footer">
    <span class="copy">Pravelo 2010 © All rights reserved.</span>
    <span class="divider"></span>
    <a href="#">Privacy Policy</a>
  </footer>
</body>
</html>
```